Need modern simple design for magazine ad, apartment and condo roofer.

I need a half page magazine ad for a local roofer to publish in an industry magazine. Apartment associations industry. All types of roofs. Shingle and Flat
Need the design to be creative and modern, clean and simple. I do not want a busy design. One that stands out and makes a point quickly.
Logo must be prominent.
DO NOT USE PHOTOS FROM MY WEBSITE PLEASE. Looking for something new.
I work on entire complexes not houses.

Need to make sure our phone number and email address are listed at the bottom. Here is my website www.vorbelan.com
Want to stay away from standard clip arts of tools, homes, apartment buildings.
Half Horizontal 7.25 x 4.75
Ads should be in PDF and JPG format.

Target Market(s)

Apartment or Condo owners looking for large scale roofing projects

Industry/Entity Type

Roofing

Requirements
Must have
• Prominent Logo
Simple Clean Design
Create graphics
Not Busy
Should not have
• Clip Art
No Photos from my website

```html
<!DOCTYPE html>
<html lang="en">
<head>
<meta charset="utf-8">
<title>Vorbelan Roofing – Half Page Ad</title>
<link rel="stylesheet" href="https://fonts.googleapis.com/css2?family=Open+Sans:ital,wght@0,400;0,600;1,800&display=swap">
<style>
  :root {
    --page-bg: #e9eaec;
    --card-bg: #eef0f2;
    --brand-blue: #1776bf;
    --ink-dark: #333537;
    --bar-grey: #58595b;
    --white: #ffffff;
  }
  * { box-sizing: border-box; margin: 0; padding: 0; }
  html, body { width: 1200px; height: 841px; overflow: hidden; background: var(--page-bg); }
  body { position: relative; font-family: "Open Sans", sans-serif; }

  .ad {
    position: absolute; left: 41px; top: 61px;
    width: 1433px; height: 922px;
    transform: scale(0.78); transform-origin: 0 0;
    background: var(--card-bg); overflow: hidden;
  }
  .photo { position: absolute; }
  .photo--courtyard { left: 0; top: 214px; width: 638px; height: 200px; background: linear-gradient(180deg, #1d3f8a 0%, #6d6250 55%, #4d5a3a 100%); }
  .photo--pool { left: 647px; top: 214px; width: 465px; height: 200px; background: linear-gradient(180deg, #8fb0d6 0%, #5d8a4e 50%, #1fa5d8 100%); }
  .photo--complex { left: 1120px; top: 214px; width: 313px; height: 200px; background: linear-gradient(180deg, #a9c6e6 0%, #8a6a52 50%, #5c6a4a 100%); }
  .photo--modern-home { left: 0; top: 424px; width: 318px; height: 204px; background: linear-gradient(180deg, #5d7080 0%, #6b5a48 50%, #b8b8b4 100%); }
  .photo--craftsman { left: 326px; top: 424px; width: 399px; height: 204px; background: linear-gradient(180deg, #9ab0c4 0%, #4a5570 50%, #5a8a3e 100%); }
  .photo--dusk-home { left: 733px; top: 424px; width: 341px; height: 204px; background: linear-gradient(180deg, #b8a8d8 0%, #3e4c7a 55%, #8a90a8 100%); }
  .photo--brick-home { left: 1081px; top: 424px; width: 352px; height: 204px; background: linear-gradient(180deg, #5e9ad8 0%, #7a5a4a 55%, #6f8a4e 100%); }

  .tag-shadow { position: absolute; left: 0; top: 0; width: 1433px; height: 922px; }

  .headline {
    position: absolute; left: 93px; top: 140px; width: 335px;
    font-style: italic; font-weight: 800; color: var(--ink-dark);
    text-align: center; line-height: 1;
  }
  .headline__lead { display: block; font-size: 34px; letter-spacing: -0.5px; }
  .headline__lead em { color: var(--brand-blue); font-style: italic; }
  .headline__main { display: block; font-size: 58px; margin-top: 4px; margin-left: -10px; }

  .brand {
    position: absolute; left: 920px; top: 100px;
    display: flex; align-items: center; gap: 16px;
  }
  .brand__mark { width: 46px; height: 46px; background: var(--brand-blue); }
  .brand__name { font-size: 46px; font-weight: 600; color: var(--brand-blue); letter-spacing: -0.5px; }

  .rule { position: absolute; left: 0; top: 645px; width: 1433px; height: 15px; background: var(--brand-blue); }

  .services {
    position: absolute; left: 0; top: 662px; width: 1433px; height: 153px;
    background: var(--brand-blue); display: flex;
  }
  .services__col { position: relative; height: 100%; border-right: 2px solid rgba(255,255,255,0.55); }
  .services__col:last-child { border-right: none; }
  .services__col--1 { width: 390px; }
  .services__col--2 { width: 326px; }
  .services__col--3 { width: 358px; }
  .services__col--4 { width: 359px; }
  .service {
    position: absolute; display: flex; align-items: center;
    color: var(--white); font-size: 23px; white-space: nowrap;
  }
  .service svg { position: absolute; width: 48px; height: 40px; fill: none; stroke: var(--white); stroke-width: 1.6; stroke-linejoin: round; stroke-linecap: round; }

  .contact { position: absolute; left: 0; top: 815px; width: 1433px; height: 107px; display: flex; }
  .contact__address {
    width: 716px; background: var(--white); padding: 14px 48px 0 0;
    text-align: right; font-size: 25px; letter-spacing: 2px; line-height: 32px; color: var(--ink-dark);
  }
  .contact__direct { width: 717px; background: var(--bar-grey); padding: 8px 0 0 32px; color: var(--white); }
  .contact__phone { font-size: 54px; letter-spacing: 5px; line-height: 1; }
  .contact__email { font-size: 22px; letter-spacing: 11px; line-height: 1; margin-top: 2px; }
</style>
</head>
<body>
  <main class="ad">
    <div class="photo photo--courtyard" role="img" aria-label="Apartment courtyard lounge at dusk"></div>
    <div class="photo photo--pool" role="img" aria-label="Apartment clubhouse with swimming pool"></div>
    <div class="photo photo--complex" role="img" aria-label="Brick apartment complex along a street"></div>
    <div class="photo photo--modern-home" role="img" aria-label="Modern two-storey residence with driveway"></div>
    <div class="photo photo--craftsman" role="img" aria-label="Craftsman style residence with front lawn"></div>
    <div class="photo photo--dusk-home" role="img" aria-label="Residence with garages at sunset"></div>
    <div class="photo photo--brick-home" role="img" aria-label="Brick and siding residence under blue sky"></div>

    <svg class="tag-shadow" viewBox="0 0 1433 922" aria-hidden="true">
      <defs>
        <filter id="tag-drop" x="-20%" y="-20%" width="160%" height="160%">
          <feDropShadow dx="10" dy="6" stdDeviation="10" flood-color="#000" flood-opacity="0.35"/>
        </filter>
        <linearGradient id="ribbon-fill" x1="0" y1="1" x2="1" y2="0">
          <stop offset="0" stop-color="#1776bf"/>
          <stop offset="1" stop-color="#0b3f78"/>
        </linearGradient>
      </defs>
      <polygon points="93,440 428,330 93,500" fill="url(#ribbon-fill)"/>
      <polygon points="93,0 428,0 428,330 93,440" fill="#eef0f2" filter="url(#tag-drop)"/>
    </svg>

    <h1 class="headline">
      <span class="headline__lead">YOUR <em>RENOVATION</em></span>
      <span class="headline__main">TEAM</span>
    </h1>

    <div class="brand">
      <span class="brand__mark"></span>
      <span class="brand__name">Vorbelan Roofing</span>
    </div>

    <div class="rule"></div>

    <section class="services">
      <div class="services__col services__col--1">
        <div class="service" style="left:143px;top:34px;">
          <svg viewBox="0 0 48 40" style="left:-62px;top:-6px;"><path d="M24 36c-7 0-10-5-10-10 0-6 6-9 5-17 5 3 6 7 6 10 2-1 3-3 3-5 4 4 6 8 6 12 0 6-4 10-10 10z"/><path d="M24 36c-3 0-5-2-5-5 0-3 3-5 3-8 3 2 6 5 6 8s-2 5-4 5z"/></svg>
          Fire Restoration
        </div>
        <div class="service" style="left:143px;top:81px;">
          <svg viewBox="0 0 48 40" style="left:-70px;top:-10px;"><path d="M2 36 22 14 34 24"/><path d="M10 36 30 14 46 32"/><path d="M22 14h8"/></svg>
          Roofing (all types)
        </div>
      </div>
      <div class="services__col services__col--2">
        <div class="service" style="left:102px;top:34px;">
          <svg viewBox="0 0 48 40" style="left:-68px;top:-10px;"><circle cx="20" cy="17" r="13"/><circle cx="20" cy="17" r="6"/><path d="M30 27 42 38"/></svg>
          Due Diligence
        </div>
        <div class="service" style="left:102px;top:81px;">
          <svg viewBox="0 0 48 40" style="left:-70px;top:-8px;"><path d="M14 8h32L36 26H4z"/><path d="M4 26v4h32l10-18"/><path d="M8 30l-3 6M16 30l-3 6M24 30l-3 6M32 30l-3 6"/></svg>
          Concrete
        </div>
      </div>
      <div class="services__col services__col--3">
        <div class="service" style="left:89px;top:34px;">
          <svg viewBox="0 0 48 40" style="left:-60px;top:-8px;"><rect x="4" y="4" width="18" height="32"/><rect x="22" y="14" width="18" height="22"/><path d="M8 10h4M14 10h4M8 17h4M14 17h4M8 24h4M14 24h4M26 20h4M32 20h4M26 27h4M32 27h4"/></svg>
          Exterior Renovations
        </div>
        <div class="service" style="left:89px;top:81px;">
          <svg viewBox="0 0 48 40" style="left:-64px;top:-18px;"><path d="M22 4h20l4 6-8 6H20z"/><path d="M30 16 18 28"/><path d="M18 28l-4 4-8 8-4-4 8-8 4-4z"/></svg>
          Paint
        </div>
      </div>
      <div class="services__col services__col--4">
        <div class="service" style="left:93px;top:34px;">
          <svg viewBox="0 0 48 40" style="left:-80px;top:-14px;"><path d="M2 26 38 8l8 6-36 18z"/><path d="M2 26v4l8 6 36-18v-4"/><path d="M14 22l10-5M20 25l10-5"/></svg>
          Wood Replacement
        </div>
        <div class="service" style="left:93px;top:81px;">More.....</div>
      </div>
    </section>

    <footer class="contact">
      <address class="contact__address" style="font-style:normal;">
        214 Harlow Avenue, Suite 300<br>Fairbrook, TX 75001
      </address>
      <div class="contact__direct">
        <div class="contact__phone">555.014.2290</div>
        <div class="contact__email">info@vorbelan.com</div>
      </div>
    </footer>
  </main>
</body>
</html>
```